Bref créative
business card for vegan prepared foods company
ZELO, taste the bright side
Simple
Petra Valdoni
Chef/Owner
www.zelofoods.example
zelofoods@mailbox.example
I would my business card to have on one side logo+web address, on the other side logo+ the rest of the info
logo and website address

```html
<!DOCTYPE html>
<html lang="en">
<head>
<meta charset="utf-8">
<title>Zelo — Business Card</title>
<link href="https://fonts.googleapis.com/css2?family=Open+Sans:wght@400;600&display=swap" rel="stylesheet">
<style>
  :root {
    --backdrop: #ece9e4;
    --card: #ffffff;
    --leaf-green: #3f9a4c;
    --earth-brown: #5a4a3d;
    --text-grey: #4a4440;
    --icon-fill: #6b5a4c;
  }
  * { box-sizing: border-box; margin: 0; padding: 0; }
  html, body {
    width: 1200px;
    height: 900px;
    overflow: hidden;
    background: var(--backdrop);
    font-family: "Open Sans", Arial, sans-serif;
  }
  .business-card {
    position: absolute;
    left: 180px;
    top: 210px;
    width: 840px;
    height: 480px;
    background: var(--card);
    box-shadow: 0 6px 24px rgba(0,0,0,0.12);
  }
  .brand {
    position: absolute;
    top: 70px;
    left: 0;
    width: 100%;
    text-align: center;
  }
  .brand-name {
    display: inline-flex;
    align-items: center;
    gap: 14px;
    font-size: 64px;
    font-weight: 600;
    letter-spacing: 4px;
    color: var(--leaf-green);
    line-height: 1;
  }
  .brand-dot {
    width: 22px;
    height: 22px;
    border-radius: 50%;
    background: var(--earth-brown);
  }
  .brand-tagline {
    margin-top: 10px;
    font-size: 17px;
    font-weight: 400;
    color: var(--leaf-green);
  }
  .person {
    position: absolute;
    top: 270px;
    left: 0;
    width: 100%;
    text-align: center;
    font-size: 26px;
    color: var(--earth-brown);
  }
  .person-name { font-weight: 600; }
  .person-divider { margin: 0 10px; font-weight: 400; }
  .person-role { font-weight: 400; font-size: 23px; }
  .contacts {
    position: absolute;
    top: 340px;
    left: 215px;
    display: grid;
    grid-template-columns: 200px 260px;
    column-gap: 22px;
    row-gap: 10px;
    font-size: 19px;
    color: var(--text-grey);
  }
  .contact-item {
    display: flex;
    align-items: center;
    gap: 10px;
    white-space: nowrap;
  }
  .contact-icon { width: 22px; height: 22px; flex: none; }
</style>
</head>
<body>
  <article class="business-card">
    <header class="brand">
      <div class="brand-name"><span>ZELO</span><span class="brand-dot"></span></div>
      <p class="brand-tagline">taste the bright side</p>
    </header>

    <p class="person">
      <span class="person-name">Petra Valdoni</span><span class="person-divider">|</span><span class="person-role">Chef/Owner</span>
    </p>

    <ul class="contacts" style="list-style:none">
      <li class="contact-item">
        <svg class="contact-icon" viewBox="0 0 22 22" aria-hidden="true">
          <circle cx="11" cy="11" r="11" fill="var(--icon-fill)"/>
          <path d="M7.5 6c.6-.6 1.3-.4 1.6.2l.9 1.8c.2.5 0 1-.4 1.3l-.6.4c.5 1.2 1.5 2.2 2.7 2.7l.4-.6c.3-.4.8-.6 1.3-.4l1.8.9c.6.3.8 1 .2 1.6l-.8.8c-.8.8-2.6.4-4.6-1.6S5.9 7.6 6.7 6.8z" fill="#fff"/>
        </svg>
        <span>555.014.2638</span>
      </li>
      <li class="contact-item">
        <svg class="contact-icon" viewBox="0 0 22 22" aria-hidden="true">
          <circle cx="11" cy="11" r="11" fill="var(--icon-fill)"/>
          <rect x="5.5" y="7" width="11" height="8" rx="1" fill="#fff"/>
          <path d="M5.8 7.4 11 11.5l5.2-4.1" stroke="var(--icon-fill)" stroke-width="1.2" fill="none"/>
        </svg>
        <span>zelofoods@mailbox.example</span>
      </li>
      <li class="contact-item">
        <svg class="contact-icon" viewBox="0 0 22 22" aria-hidden="true">
          <circle cx="11" cy="11" r="11" fill="var(--icon-fill)"/>
          <rect x="6" y="6" width="10" height="10" rx="1.5" fill="#fff"/>
          <rect x="8" y="8" width="6" height="2.5" fill="var(--icon-fill)"/>
          <rect x="8" y="12" width="6" height="2" fill="var(--icon-fill)"/>
        </svg>
        <span>555.019.4417</span>
      </li>
      <li class="contact-item">
        <svg class="contact-icon" viewBox="0 0 22 22" aria-hidden="true">
          <circle cx="11" cy="11" r="11" fill="var(--icon-fill)"/>
          <circle cx="11" cy="11" r="5.5" fill="none" stroke="#fff" stroke-width="1.3"/>
          <ellipse cx="11" cy="11" rx="2.4" ry="5.5" fill="none" stroke="#fff" stroke-width="1.1"/>
          <path d="M5.5 11h11" stroke="#fff" stroke-width="1.1"/>
        </svg>
        <span>www.zelofoods.example</span>
      </li>
    </ul>
  </article>
</body>
</html>
```